I need a website, primarily a landing page, for my company, Harlow Ridge. A sales training and cons

I need a web design/landing page for a new sales training and consulting company, harlow ridge. We perform "sales experiments" aimed at each individual or team, where we assist in helping them identify their strengths, through a series of "sales experiments" that we can tailor based on the individual and what they're trying to accomplish.

```html
<!DOCTYPE html>
<html lang="en">
<head>
<meta charset="utf-8">
<title>Harlow Ridge — Sales Experiments</title>
<link rel="stylesheet" href="https://fonts.googleapis.com/css2?family=Open+Sans:wght@400;600&display=swap">
<style>
  :root {
    --page-bg: #ffffff;
    --nav-text: #333333;
    --nav-active: #3a6ea5;
    --brand: #2f6fae;
    --heading: #1f1f1f;
    --body-text: #666666;
    --icon: #3d7ab8;
    --helix-light: #eef6fc;
    --helix-mid: #dcecf8;
    --button-dark: #2b2b2b;
    --scroll-bar: #8a8a8a;
    --frame-edge: #ececec;
  }
  * { margin: 0; padding: 0; box-sizing: border-box; }
  html, body { width: 1200px; height: 675px; overflow: hidden; background: var(--page-bg); }
  body { font-family: "Open Sans", Arial, sans-serif; position: relative; }

  .site {
    position: absolute; left: 123px; top: 68px; width: 978px; height: 562px;
    background: var(--page-bg); overflow: hidden;
    border-right: 1px solid var(--frame-edge);
  }
  .hero-art {
    position: absolute; left: 0; top: 62px; width: 978px; height: 500px;
    background:
      radial-gradient(ellipse 420px 110px at 330px 170px, var(--helix-mid), transparent 70%),
      radial-gradient(ellipse 360px 120px at 760px 330px, var(--helix-mid), transparent 70%),
      linear-gradient(160deg, var(--helix-light) 0%, #f7fbfe 55%, var(--helix-light) 100%);
  }

  .site-nav {
    position: absolute; left: 0; top: 0; width: 978px; height: 62px;
    background: var(--page-bg); box-shadow: 0 2px 6px rgba(0,0,0,0.07); z-index: 2;
  }
  .nav-link {
    position: absolute; top: 21px; font-size: 13px; line-height: 18px;
    color: var(--nav-text); text-decoration: none; white-space: nowrap;
  }
  .nav-link.is-active { color: var(--nav-active); }
  .brand {
    position: absolute; left: 488px; top: 20px; width: 0; display: flex;
    justify-content: center; align-items: center; gap: 6px;
  }
  .brand-inner { display: flex; align-items: center; gap: 6px; white-space: nowrap; }
  .brand-dot { width: 10px; height: 10px; border-radius: 50%; background: var(--brand); }
  .brand-name { font-size: 14px; font-weight: 600; color: var(--brand); letter-spacing: 0.3px; }

  .feature { position: absolute; width: 270px; }
  .feature-head { display: flex; align-items: flex-end; gap: 10px; height: 34px; }
  .feature-icon { width: 34px; height: 34px; flex: none; }
  .feature-title { font-size: 19.5px; font-weight: 400; color: var(--heading); line-height: 24px; }
  .feature-text { margin-top: 6px; font-size: 13.5px; line-height: 21px; color: var(--body-text); }

  .scroll-track {
    position: absolute; left: 976px; top: 131px; width: 2px; height: 60px; background: var(--scroll-bar);
  }
  .back-to-top {
    position: absolute; left: 924px; top: 525px; width: 38px; height: 38px; border-radius: 50%;
    background: var(--button-dark); display: flex; align-items: center; justify-content: center;
  }
</style>
</head>
<body>
  <div class="site">
    <div class="hero-art" role="img" aria-label="Soft pale blue DNA double helix illustration spanning the background"></div>

    <nav class="site-nav">
      <a class="nav-link" style="left:57px">Home</a>
      <a class="nav-link is-active" style="left:134px">About Harlow Ridge</a>
      <a class="nav-link" style="left:298px">About me</a>
      <div class="brand"><div class="brand-inner"><span class="brand-dot"></span><span class="brand-name">HARLOW RIDGE</span></div></div>
      <a class="nav-link" style="left:687px">Experiments</a>
      <a class="nav-link" style="left:805px">Blog</a>
      <a class="nav-link" style="left:871px">Contact</a>
    </nav>

    <section class="features">
      <article class="feature" style="left:37px; top:172px">
        <div class="feature-head">
          <svg class="feature-icon" viewBox="0 0 34 34" fill="none" stroke="var(--icon)" stroke-width="1.4">
            <rect x="3" y="13" width="28" height="8" transform="rotate(-45 17 17)"/>
            <path d="M6 28 L10 20 L26 4 L30 8 L14 24 Z"/>
            <path d="M6 28 L14 24"/>
          </svg>
          <h3 class="feature-title">Feature One</h3>
        </div>
        <p class="feature-text">Lorem ipsum dolor sit amet, consectetur adipiscing elit, sed do eiusmod tempor incididunt ut labore et dolore.</p>
      </article>

      <article class="feature" style="left:358px; top:172px">
        <div class="feature-head">
          <svg class="feature-icon" viewBox="0 0 34 34" fill="none" stroke="var(--icon)" stroke-width="1.4">
            <path d="M17 3 C8 3 4 9 4 14 C4 20 12 24 14 26 H20 C22 24 30 20 30 14 C30 9 26 3 17 3 Z"/>
            <path d="M17 3 C12 8 12 20 14 26 M17 3 C22 8 22 20 20 26"/>
            <rect x="14" y="28" width="6" height="4"/>
          </svg>
          <h3 class="feature-title">Feature two</h3>
        </div>
        <p class="feature-text">Lorem ipsum dolor sit amet, consectetur adipiscing elit, sed do eiusmod tempor incididunt ut labore et dolore.</p>
      </article>

      <article class="feature" style="left:678px; top:172px">
        <div class="feature-head">
          <svg class="feature-icon" viewBox="0 0 34 34" fill="none" stroke="var(--icon)" stroke-width="1.4">
            <path d="M17 4 L32 11 L17 18 L2 11 Z"/>
            <path d="M2 17 L17 24 L32 17"/>
            <path d="M2 23 L17 30 L32 23"/>
          </svg>
          <h3 class="feature-title">Feature three</h3>
        </div>
        <p class="feature-text">Lorem ipsum dolor sit amet, consectetur adipiscing elit, sed do eiusmod tempor incididunt ut labore et dolore.</p>
      </article>

      <article class="feature" style="left:37px; top:366px">
        <div class="feature-head">
          <svg class="feature-icon" viewBox="0 0 34 34" fill="none" stroke="var(--icon)" stroke-width="1.4">
            <path d="M17 4 L32 11 L17 18 L2 11 Z"/>
            <path d="M2 17 L17 24 L32 17"/>
            <path d="M2 23 L17 30 L32 23"/>
          </svg>
          <h3 class="feature-title">Feature four</h3>
        </div>
        <p class="feature-text">Lorem ipsum dolor sit amet, consectetur adipiscing elit, sed do eiusmod tempor incididunt ut labore et dolore.</p>
      </article>

      <article class="feature" style="left:358px; top:366px">
        <div class="feature-head">
          <svg class="feature-icon" viewBox="0 0 34 34" fill="none" stroke="var(--icon)" stroke-width="1.4">
            <path d="M6 26 L9 18 L24 3 L30 9 L15 24 Z"/>
            <path d="M6 26 L15 24 M21 6 L27 12"/>
            <path d="M1 32 H33"/>
          </svg>
          <h3 class="feature-title">Feature five</h3>
        </div>
        <p class="feature-text">Lorem ipsum dolor sit amet, consectetur adipiscing elit, sed do eiusmod tempor incididunt ut labore et dolore.</p>
      </article>

      <article class="feature" style="left:678px; top:366px">
        <div class="feature-head">
          <svg class="feature-icon" viewBox="0 0 34 34" fill="none" stroke="var(--icon)" stroke-width="1.4">
            <circle cx="17" cy="5" r="3"/>
            <path d="M17 8 V31 M11 13 H23"/>
            <path d="M3 20 C4 27 10 31 17 31 C24 31 30 27 31 20"/>
            <path d="M1 23 L3 19 L6 22 M33 23 L31 19 L28 22"/>
          </svg>
          <h3 class="feature-title">Feature six</h3>
        </div>
        <p class="feature-text">Lorem ipsum dolor sit amet, consectetur adipiscing elit, sed do eiusmod tempor incididunt ut labore et dolore.</p>
      </article>
    </section>

    <div class="scroll-track"></div>
    <a class="back-to-top" aria-label="Back to top">
      <svg width="14" height="14" viewBox="0 0 14 14" fill="none" stroke="#ffffff" stroke-width="2">
        <path d="M3 9 L7 5 L11 9"/>
      </svg>
    </a>
  </div>
</body>
</html>
```